We are Here! Come and Meet the Team Flyer

A clear and quirky, flyer to let local Residents know we have landed.
Based around our logo.

We avoid anything medical but rather focus on being pet-centred, warmth, approachable and community-orientated.

We pride ourselves on being cutting-edge but steer away from a cold sterile image.
Approachability, uptodate. We understandt hat pets are part of a family and we will provide the level of care that we would expect for our own pets.

Target Market(s)

Residents in the area

Industry/Entity Type

Veterinary

Font styles to use
Sans Serif

Colors
33b8a4
ffc214
0255a3

Requirements
Must have
• Logo and PERHAPS a location of Clinic indicated on the cat of the Logo.
• NOW OPEN!
• 1) Exact location of the Clinic indicated: the lefthand side of tail, near the cat's back.
• 2) Warm, quirky, Approachable
• 3) Contact details (see attached draft Poster)
• 4) Location: Silver Brook Arcade, Building 4, Mezzanine level
Should not have
• nothing medical or cliched.

```html
<!DOCTYPE html>
<html lang="en">
<head>
<meta charset="utf-8">
<title>Happy Tails Haven – Now Open Flyer</title>
<link rel="stylesheet" href="https://fonts.googleapis.com/css2?family=Open+Sans:wght@400;600;700;800&display=swap">
<style>
  :root {
    --teal: #33b8a4;
    --teal-light: #45c6b2;
    --yellow: #ffc214;
    --blue: #0255a3;
    --white: #ffffff;
    --ink: #111111;
    --photo-light: #f1eeea;
    --photo-mid: #d9d2c8;
  }
  * { margin: 0; padding: 0; box-sizing: border-box; }
  html, body { width: 986px; height: 1200px; overflow: hidden; }
  body { font-family: "Open Sans", sans-serif; color: var(--white); }

  .flyer { position: relative; width: 986px; height: 1200px; overflow: hidden; }
  .flyer-shapes { position: absolute; inset: 0; }

  .brand { position: absolute; left: 24px; top: 70px; display: flex; align-items: center; gap: 14px; }
  .brand-mark { width: 48px; height: 48px; border: 4px solid var(--blue); border-radius: 50%; }
  .brand-text { display: flex; flex-direction: column; }
  .brand-name { font-size: 40px; font-weight: 600; color: var(--blue); letter-spacing: -0.5px; line-height: 1; }
  .brand-tag { font-size: 11px; font-weight: 400; color: var(--blue); letter-spacing: 4px; margin-top: 6px; text-transform: uppercase; }

  .teaser { position: absolute; left: 164px; top: 564px; width: 633px; height: 90px;
    background: var(--white); display: flex; align-items: center; justify-content: center;
    box-shadow: 0 3px 6px rgba(0,0,0,0.15); }
  .teaser h2 { font-size: 44px; font-weight: 800; color: var(--blue); letter-spacing: 2px; }

  .announce { position: absolute; left: 0; right: 0; top: 708px; text-align: center; }
  .announce-place { font-size: 58px; font-weight: 700; letter-spacing: 2px; line-height: 1; }
  .announce-sub { font-size: 34px; font-weight: 400; letter-spacing: 1px; margin-top: 8px; }
  .announce-rule { width: 864px; height: 5px; background: var(--yellow); margin: 10px auto 0; }
  .announce-hours { font-size: 44px; font-weight: 700; letter-spacing: 3px; margin-top: 12px; }

  .contact-label { position: absolute; left: 427px; top: 926px; width: 152px; height: 30px;
    background: var(--ink); font-size: 17px; font-weight: 700; letter-spacing: 1px;
    display: flex; align-items: center; justify-content: center; }

  .contact-item { position: absolute; display: flex; align-items: flex-start; gap: 14px;
    font-size: 16px; font-weight: 600; letter-spacing: 0.6px; line-height: 1.35; }
  .contact-item svg { flex: none; }
  .contact-address { left: 150px; top: 990px; }
  .contact-phone { left: 150px; top: 1078px; align-items: center; }
  .contact-email { left: 590px; top: 976px; align-items: center; }
  .contact-web { left: 590px; top: 1052px; align-items: center; }

  .social { position: absolute; right: 24px; bottom: 50px; display: flex; gap: 14px;
    font-size: 10px; font-weight: 600; color: var(--ink); }
  .social-handle { display: flex; align-items: center; gap: 4px; }
  .social-handle i { display: block; width: 10px; height: 10px; background: var(--blue); }
</style>
</head>
<body>
<main class="flyer">
  <svg class="flyer-shapes" width="986" height="1200" viewBox="0 0 986 1200">
    <defs>
      <linearGradient id="photoTone" x1="0" y1="0" x2="1" y2="1">
        <stop offset="0" stop-color="var(--photo-light)"/>
        <stop offset="0.6" stop-color="#ebe6df"/>
        <stop offset="1" stop-color="var(--photo-mid)"/>
      </linearGradient>
    </defs>
    <rect class="bg-top" width="986" height="700" fill="var(--yellow)"/>
    <polygon class="hero-photo" role="img"
      aria-label="Photo: a smiling young girl lying on a soft rug beside a fluffy cream puppy"
      points="0,322 340,262 400,200 986,200 986,590 0,590" fill="url(#photoTone)"/>
    <polygon class="band-left" points="0,528 250,590 0,590" fill="var(--teal)"/>
    <rect class="band-yellow" y="590" width="986" height="100" fill="var(--yellow)"/>
    <polygon class="band-right" points="986,560 986,690 830,690 900,610 760,610 800,590" fill="var(--teal)"/>
    <rect class="bg-bottom" y="690" width="986" height="510" fill="var(--teal-light)"/>
    <polygon class="band-corner" points="600,1200 676,1116 986,1116 986,1200" fill="var(--yellow)"/>
  </svg>

  <header class="brand">
    <span class="brand-mark"></span>
    <div class="brand-text">
      <span class="brand-name">happy tails haven</span>
      <span class="brand-tag">Veterinary Clinic</span>
    </div>
  </header>

  <div class="teaser"><h2>DID YOU KNOW?</h2></div>

  <section class="announce">
    <h1 class="announce-place">Harbour Crescent</h1>
    <p class="announce-sub">now has its own Veterinary Clinic</p>
    <div class="announce-rule"></div>
    <p class="announce-hours">OPEN 7 DAYS A WEEK</p>
  </section>

  <div class="contact-label">Contact Us</div>

  <div class="contact-item contact-address">
    <svg width="36" height="44" viewBox="0 0 36 44"><path d="M18 2a15 15 0 0 0-15 15c0 11 15 25 15 25s15-14 15-25A15 15 0 0 0 18 2z" fill="var(--white)"/><circle cx="18" cy="17" r="6" fill="var(--teal-light)"/></svg>
    <p>Mezzanine level, Building 4,<br>Silver Brook Arcade<br>(Above Cafe Lumo)</p>
  </div>

  <div class="contact-item contact-phone">
    <svg width="40" height="40" viewBox="0 0 40 40" fill="none" stroke="var(--white)" stroke-width="3" stroke-linecap="round"><path d="M9 5l6 8-4 4c2 5 6 9 11 11l4-4 8 6-4 6C18 36 4 22 4 11z" fill="var(--white)" stroke="none"/><path d="M24 10a8 8 0 0 1 6 6M25 4a14 14 0 0 1 11 11"/></svg>
    <p>800-HTH-VET/04 5550192</p>
  </div>

  <div class="contact-item contact-email">
    <svg width="40" height="28" viewBox="0 0 40 28" fill="none" stroke="var(--white)" stroke-width="2.5"><rect x="2" y="2" width="36" height="24"/><path d="M2 2l18 14L38 2"/></svg>
    <p>info@happytailshaven.ae</p>
  </div>

  <div class="contact-item contact-web">
    <svg width="40" height="40" viewBox="0 0 40 40" fill="none" stroke="var(--white)" stroke-width="2.5"><circle cx="20" cy="20" r="17"/><ellipse cx="20" cy="20" rx="7" ry="17"/><path d="M3 20h34M6 11h28M6 29h28"/></svg>
    <p>www.happytailshaven.ae</p>
  </div>

  <div class="social">
    <span class="social-handle"><i></i>@HTHVetsHarbour</span>
    <span class="social-handle"><i></i>@happytailsvet</span>
    <span class="social-handle"><i></i>@hthvetclinic</span>
  </div>
</main>
</body>
</html>
```